Powerpoint template for technical & business level presentations

Looking for a powerpoint template to use for professional business & technical presentations that will work well with the logo you designed for us.

Industry/Entity Type

Business

```html
<!DOCTYPE html>
<html lang="en">
<head>
<meta charset="utf-8">
<title>Graphic Slide Template</title>
<link rel="stylesheet" href="https://fonts.googleapis.com/css2?family=Graduate&family=Open+Sans:wght@400;700&display=swap">
<style>
  :root {
    --page: #ffffff;
    --slide-light: #eeeeee;
    --slide-mid: #dcdcdc;
    --ink: #333333;
    --band: #232323;
    --blue: #29a8e0;
    --blue-dark: #1b75bb;
    --lime: #8cc63f;
    --green: #3ab54a;
    --green-dark: #0e9444;
    --green-mid: #2db671;
    --teal: #13a89e;
    --grey: #58585a;
    --grey-dark: #3d3d3f;
    --grey-pie: #6d6e71;
    --tan: #c49a6c;
    --tan-dark: #a67c52;
    --white: #ffffff;
  }
  * { margin: 0; padding: 0; box-sizing: border-box; }
  html, body { width: 1200px; height: 900px; overflow: hidden; background: var(--page); }
  .canvas { position: relative; width: 1200px; height: 900px; }

  .slide {
    position: absolute; left: 48px; top: 176px; width: 1104px; height: 620px;
    background: radial-gradient(ellipse at 45% 40%, var(--slide-light), var(--slide-mid));
    overflow: hidden;
  }
  .slide-art { position: absolute; left: 0; top: 0; width: 1104px; height: 620px; }

  .page-number {
    position: absolute; right: 26px; top: 30px;
    font-family: "Graduate", serif; font-size: 22px; font-weight: 700; color: var(--white);
  }

  .title-band {
    position: absolute; left: 16px; top: 472px; width: 1072px; height: 136px;
    background: var(--band);
  }
  .slide-title {
    position: absolute; left: 22px; top: 14px;
    font-family: "Graduate", serif; font-size: 61px; font-weight: 400; line-height: 1;
    color: var(--blue); letter-spacing: 2.5px; white-space: nowrap;
    -webkit-text-stroke: 1.5px var(--blue);
  }
  .title-rule {
    position: absolute; left: 22px; top: 88px; width: 486px; height: 3px; background: var(--white);
  }
  .slide-subtitle {
    position: absolute; left: 76px; top: 97px;
    font-family: "Open Sans", sans-serif; font-size: 17px; color: var(--white); white-space: nowrap;
  }
  .contact {
    position: absolute; right: 198px; top: 94px; text-align: right;
    font-family: "Open Sans", sans-serif; font-size: 11.5px; line-height: 17px; color: var(--white);
  }
  .brand {
    position: absolute; right: 10px; top: 101px;
    display: flex; align-items: center; gap: 8px;
    font-family: "Open Sans", sans-serif; font-weight: 700; font-size: 16px;
    color: var(--white); white-space: nowrap;
  }
  .brand-mark { width: 12px; height: 12px; background: var(--blue); }
</style>
</head>
<body>
<div class="canvas">
  <section class="slide">
    <svg class="slide-art" viewBox="48 176 1104 620" aria-hidden="true">
      <line x1="92" y1="232" x2="1018" y2="232" stroke="var(--ink)" stroke-width="4"/>
      <rect x="80" y="220" width="24" height="24" rx="4" transform="rotate(45 92 232)" fill="var(--white)" stroke="var(--ink)" stroke-width="3"/>
      <circle cx="92" cy="232" r="7" fill="var(--blue)"/>
      <polygon points="1038,188 1138,188 1138,286" fill="var(--blue)"/>

      <g class="pyramid">
        <polygon points="346,354 286,422 406,422" fill="var(--lime)"/>
        <polygon points="286,422 406,422 402,432 290,432" fill="var(--green)"/>
        <polygon points="290,432 402,432 486,504 206,504" fill="var(--blue)"/>
        <polygon points="206,504 486,504 476,513 216,513" fill="var(--blue-dark)"/>
        <polygon points="230,513 490,513 566,582 128,582" fill="var(--grey)"/>
        <polygon points="128,582 566,582 548,608 146,608" fill="var(--grey-dark)"/>
      </g>

      <g class="pie" stroke-linejoin="round">
        <path d="M852,466 L1008,466 A160 160 0 0 1 932,610 Z" fill="var(--blue-dark)"/>
        <path d="M842,466 L764,604 A160 160 0 0 1 684,466 Z" fill="var(--grey-dark)"/>
        <path d="M846,476 L926,616 A160 160 0 0 1 770,614 Z" fill="var(--tan-dark)"/>

        <g stroke="#000" stroke-width="4">
          <path d="M846,454 L740,338 A160 160 0 0 1 846,296 Z" fill="var(--green-dark)"/>
          <path d="M846,454 L846,296 A160 160 0 0 1 962,346 Z" fill="var(--green-mid)"/>
          <path d="M846,454 L962,346 A160 160 0 0 1 1006,454 Z" fill="var(--teal)"/>
          <path d="M846,454 L1006,454 A160 160 0 0 1 928,598 Z" fill="var(--blue)"/>
          <path d="M846,454 L768,594 A160 160 0 0 1 686,454 Z" fill="var(--grey-pie)"/>
          <path d="M846,454 L686,454 A160 160 0 0 1 740,338 Z" fill="var(--lime)"/>
          <path d="M846,454 L928,598 A160 160 0 0 1 768,594 Z" fill="var(--tan)"/>
        </g>
      </g>
    </svg>

    <div class="page-number">04</div>

    <div class="title-band">
      <h1 class="slide-title">GRAPHIC SLIDE</h1>
      <div class="title-rule"></div>
      <p class="slide-subtitle">DETAILS OF SLIDE / NAME OF PRESENTOR</p>
      <p class="contact">WWW.HALVORSENADVISORY.COM<br>HELLO@HALVORSEN.COM</p>
      <p class="brand"><span class="brand-mark"></span>Halvorsen Advisory</p>
    </div>
  </section>
</div>
</body>
</html>
```